Industrial Professional Business Card Design (Vantrel KX)

Would like professional looking business cards. Not too busy leaning towards minimal. Should have a slogan like:
"Industrial Automation and Control".

We are a tech company that programs industrial PLC computers. We also develop custom hardware solutions. Please use the logo for inspiration.

Target Market(s)

Mining, industrial, processing, automation, factory

Industry/Entity Type

Engineering

Contact Information for Business Card

Name, phone, email, website. job title.

Font styles to use
Other font styles liked:
• droid sans

Requirements
Must have
• Use colours that go well with the logo. Not too busy design.

```html
<!DOCTYPE html>
<html lang="en">
<head>
<meta charset="utf-8">
<title>Vantrel KX Business Card</title>
<link rel="stylesheet" href="https://fonts.googleapis.com/css2?family=Noto+Sans:wght@400;500;700&display=swap">
<style>
  :root {
    --backdrop: #2b2b2b;
    --navy-deep: #17215a;
    --navy-mid: #1f2f7a;
    --navy-light: #2c3f9c;
    --paper: #f3f3f3;
    --orange: #ee6a1f;
    --steel-blue: #1f5f8b;
    --ink-navy: #1c3f6e;
    --ink-grey: #333a40;
    --white: #ffffff;
  }
  * { box-sizing: border-box; margin: 0; padding: 0; }
  html, body {
    width: 1102px;
    height: 1200px;
    overflow: hidden;
    background: var(--backdrop);
    font-family: "Noto Sans", sans-serif;
  }
  .sheet {
    position: relative;
    width: 1102px;
    height: 1200px;
  }
  .card {
    position: absolute;
    left: 201px;
    width: 700px;
    height: 400px;
    border-radius: 30px;
    overflow: hidden;
  }
  .card-front {
    top: 170px;
    background: radial-gradient(ellipse at 30% 20%, var(--navy-mid) 0%, var(--navy-deep) 75%);
  }
  .front-decoration {
    position: absolute;
    right: 0;
    top: 0;
    width: 340px;
    height: 400px;
    background: radial-gradient(circle at 85% 45%, var(--navy-deep) 0%, var(--navy-light) 55%, rgba(44,63,156,0) 80%);
    opacity: 0.75;
  }
  .front-brand {
    position: absolute;
    left: 46px;
    top: 268px;
    color: var(--white);
    font-weight: 500;
    font-size: 50px;
    letter-spacing: -0.5px;
    line-height: 1;
  }
  .front-tagline {
    position: absolute;
    left: 47px;
    top: 338px;
    color: var(--white);
    font-size: 18px;
    line-height: 1;
  }
  .card-back {
    top: 630px;
    background: var(--paper);
  }
  .holder-name {
    position: absolute;
    left: 70px;
    top: 94px;
    color: var(--steel-blue);
    font-weight: 700;
    font-size: 23px;
    letter-spacing: 0.3px;
    line-height: 1;
  }
  .holder-title {
    position: absolute;
    left: 70px;
    top: 122px;
    color: var(--ink-grey);
    font-size: 16px;
    line-height: 1;
  }
  .contact-list {
    position: absolute;
    left: 70px;
    top: 273px;
    list-style: none;
  }
  .contact-item {
    display: flex;
    align-items: center;
    gap: 8px;
    height: 24px;
    color: var(--ink-grey);
    font-size: 16px;
  }
  .contact-icon { width: 14px; height: 14px; flex: none; }
  .back-brand {
    position: absolute;
    left: 421px;
    top: 302px;
    color: var(--ink-navy);
    font-weight: 500;
    font-size: 37px;
    letter-spacing: -0.4px;
    line-height: 1;
  }
</style>
</head>
<body>
<main class="sheet">
  <section class="card card-front">
    <div class="front-decoration" role="img" aria-label="Large embossed gear decoration with circuit nodes"></div>
    <div class="front-brand">Vantrel KX</div>
    <div class="front-tagline">Industrial Automation and Control</div>
  </section>

  <section class="card card-back">
    <h1 class="holder-name">DORIAN KELL</h1>
    <p class="holder-title">President</p>
    <ul class="contact-list">
      <li class="contact-item">
        <svg class="contact-icon" viewBox="0 0 16 16" aria-hidden="true"><path fill="var(--orange)" d="M3.5 1.5l2.5 3-1.5 1.7c.8 1.8 2.2 3.2 4 4L10.2 8.7l3 2.5-1.4 2.6c-5.3-.3-9.6-4.6-9.9-9.9z"/></svg>
        <span>555-014-2278</span>
      </li>
      <li class="contact-item">
        <svg class="contact-icon" viewBox="0 0 16 16" aria-hidden="true"><rect x="1" y="3.5" width="14" height="9" fill="var(--orange)"/><path d="M1 3.5l7 5 7-5" fill="none" stroke="var(--paper)" stroke-width="1.3"/></svg>
        <span>hello@vantrelkx.com</span>
      </li>
      <li class="contact-item">
        <svg class="contact-icon" viewBox="0 0 16 16" aria-hidden="true"><circle cx="8" cy="8" r="6.5" fill="var(--orange)"/><path d="M1.5 8h13M8 1.5c-2.5 3-2.5 10 0 13M8 1.5c2.5 3 2.5 10 0 13" fill="none" stroke="var(--paper)" stroke-width="1"/></svg>
        <span>www.vantrelkx.com</span>
      </li>
    </ul>
    <div class="back-brand">Vantrel KX</div>
  </section>
</main>
</body>
</html>
```